Redesign business cards

We have a new logo and I am not that happy with the layout of our existing card and looking for a change. Font is a bit small and the green can be hard to read. Logo may need a tidy up as the copy I have is not that hi-res too so require you to produce a hi-res version of the logo for us too. There will be three individual business cards to produce with just the names and phone numbers being different. Address will change too, but use what you see on the card for now.

Industry/Entity Type

Business

Requirements
Nice to have
• You could consider a redesign to the new logo, just not too radical. We like the blue and green hexagons as we feel that they are representative of oil industry that we are in.

```html
<!DOCTYPE html>
<html lang="en">
<head>
<meta charset="utf-8">
<title>Verdan Oil Services – Business Card</title>
<link rel="stylesheet" href="https://fonts.googleapis.com/css2?family=Open+Sans:wght@400;600;700&display=swap">
<style>
  :root {
    --page-bg: #c9ccd0;
    --card-white: #ffffff;
    --card-mist: #dfe0e2;
    --brand-green: #8dc63f;
    --brand-grey: #676a6e;
    --logo-grey: #5c5f63;
    --text-light: #ffffff;
  }
  * { margin: 0; padding: 0; box-sizing: border-box; }
  html, body {
    width: 1200px;
    height: 865px;
    overflow: hidden;
  }
  body {
    background: var(--page-bg);
    font-family: "Open Sans", Arial, sans-serif;
    position: relative;
  }
  .business-card {
    position: absolute;
    left: 100px;
    top: 147px;
    width: 1000px;
    height: 571px;
    background: radial-gradient(ellipse at 30% 45%, var(--card-white) 0%, var(--card-white) 40%, var(--card-mist) 100%);
    box-shadow: 0 14px 30px rgba(0,0,0,0.25);
    overflow: hidden;
  }
  .card-shapes {
    position: absolute;
    inset: 0;
    width: 100%;
    height: 100%;
  }
  .company-mark {
    position: absolute;
    left: 90px;
    top: 225px;
    display: flex;
    align-items: center;
    gap: 22px;
    color: var(--logo-grey);
    font-weight: 600;
  }
  .company-mark__square {
    width: 78px;
    height: 78px;
    background: var(--brand-green);
  }
  .company-mark__name {
    display: flex;
    flex-direction: column;
    line-height: 1;
  }
  .company-mark__title {
    font-size: 74px;
    letter-spacing: -1px;
  }
  .company-mark__tagline {
    font-size: 30px;
    margin-top: 6px;
    padding-left: 4px;
  }
  .contact-block {
    position: absolute;
    right: 54px;
    top: 48px;
    text-align: right;
    color: var(--text-light);
  }
  .contact-block__name {
    font-size: 26px;
    font-weight: 700;
    line-height: 1.2;
  }
  .contact-block__role {
    font-size: 24px;
    font-weight: 400;
    margin-bottom: 40px;
  }
  .contact-block__line {
    font-size: 22px;
    line-height: 1.42;
    display: flex;
    justify-content: flex-end;
    align-items: center;
    gap: 8px;
  }
  .contact-block__line--web { margin-top: 2px; }
  .contact-icon {
    width: 20px;
    height: 20px;
    fill: var(--text-light);
  }
</style>
</head>
<body>
  <div class="business-card">
    <svg class="card-shapes" viewBox="0 0 1000 571" preserveAspectRatio="none" aria-hidden="true">
      <path class="green-panel" d="M430,0 L1000,0 L1000,571 L585,571 C700,400 690,170 430,0 Z" fill="var(--brand-green)"/>
      <path class="grey-swoosh" d="M548,150 C640,280 620,440 470,571 L560,571 C680,430 670,270 548,150 Z" fill="var(--brand-grey)" stroke="var(--card-white)" stroke-width="6"/>
    </svg>

    <div class="company-mark">
      <div class="company-mark__square"></div>
      <div class="company-mark__name">
        <span class="company-mark__title">Verdan</span>
        <span class="company-mark__tagline">Oil Services</span>
      </div>
    </div>

    <div class="contact-block">
      <div class="contact-block__name">Marlo Fenwick-Hale</div>
      <div class="contact-block__role">Consultant</div>
      <div class="contact-block__line">104.12th floor,Quay</div>
      <div class="contact-block__line">Harbour Road NKT</div>
      <div class="contact-block__line">014 555 0173
        <svg class="contact-icon" viewBox="0 0 24 24" aria-label="Phone"><path d="M6.6 10.8a15.2 15.2 0 0 0 6.6 6.6l2.2-2.2a1 1 0 0 1 1-.25 11.4 11.4 0 0 0 3.6.57 1 1 0 0 1 1 1V20a1 1 0 0 1-1 1A17 17 0 0 1 3 4a1 1 0 0 1 1-1h3.5a1 1 0 0 1 1 1c0 1.25.2 2.450.57 3.57a1 1 0 0 1-.25 1Z"/></svg>
      </div>
      <div class="contact-block__line">014 555 0174
        <svg class="contact-icon" viewBox="0 0 24 24" aria-label="Fax"><path d="M7 2h8l3 3v5H7Z M3 10h18v11H3Z M6 13h3v2H6Z M6 17h3v2H6Z M11 13h3v2h-3Z M11 17h3v2h-3Z M16 13h3v6h-3Z"/></svg>
      </div>
      <div class="contact-block__line">marlo@verdanoil.com
        <svg class="contact-icon" viewBox="0 0 24 24" aria-label="Email"><path d="M2 5h20v14H2Z M3.5 6.5 12 13l8.5-6.5" fill="var(--text-light)" stroke="var(--brand-green)" stroke-width="1.6"/></svg>
      </div>
      <div class="contact-block__line contact-block__line--web">www.verdanoil.com</div>
    </div>
  </div>
</body>
</html>
```